the ridgewell craft premier branch

design a DL A4 tri fold brochure to reflect our creative landscape business
my web site www.theridgewellcraft.com.au
has all the information needed
i will also be updating the website to be more updated and creative design

```html
<!DOCTYPE html>
<html lang="en">
<head>
<meta charset="utf-8">
<title>The Ridgewell Craft – DL Tri-fold Back</title>
<link href="https://fonts.googleapis.com/css2?family=Arimo:ital,wght@0,400;0,700;1,400&display=swap" rel="stylesheet">
<style>
  :root {
    --page: #ffffff;
    --panel-edge: #e2e2e4;
    --panel-mid: #f7f7f8;
    --ink: #1e1e1e;
    --ink-soft: #333333;
    --accent: #e08a1e;
    --rule: #2a2a2a;
    --pool: #3d78b0;
    --pool-deep: #1f4f86;
    --garden: #8b6a4c;
    --garden-light: #b9a88e;
  }
  * { margin: 0; padding: 0; box-sizing: border-box; }
  html, body { width: 1200px; height: 1129px; overflow: hidden; background: var(--page); }
  body { position: relative; font-family: "Arimo", Arial, sans-serif; color: var(--ink); }

  .brochure-back {
    position: absolute; left: 64px; top: 11px; width: 1047px; height: 1050px;
    background: radial-gradient(ellipse at 60% 50%, var(--panel-mid) 0%, var(--panel-edge) 100%);
  }
  .fold-line {
    position: absolute; left: 0; width: 100%; height: 0;
    border-top: 2px dashed var(--rule);
  }
  .fold-line.first { top: 348px; }
  .fold-line.second { top: 701px; }

  .project-photo { position: absolute; }
  .project-photo.toorak {
    left: 21px; top: 29px; width: 434px; height: 288px;
    background: linear-gradient(180deg, #2c4a7a 0%, #c9c3b8 45%, var(--pool) 70%, var(--pool-deep) 100%);
  }
  .project-photo.parkville {
    left: 24px; top: 374px; width: 433px; height: 287px;
    background: linear-gradient(160deg, #c8cdd3 0%, var(--garden) 35%, var(--garden-light) 60%, #5a3a26 100%);
  }

  .project-copy { position: absolute; left: 493px; width: 540px; }
  .project-copy.toorak { top: 44px; }
  .project-copy.parkville { top: 395px; }
  .project-title { font-weight: 700; font-size: 21px; letter-spacing: 0.3px; }
  .project-tagline { font-style: italic; font-size: 24px; margin-top: 19px; color: var(--ink-soft); }
  .project-details { margin-top: 21px; font-size: 18.5px; line-height: 22.3px; color: var(--ink-soft); }
  .project-details ul { list-style: none; }
  .project-details li::before { content: "• "; font-size: 14px; }

  .brand-mark {
    position: absolute; left: 130px; top: 840px; width: 290px; text-align: center;
  }
  .brand-mark .dot {
    display: block; width: 90px; height: 90px; border-radius: 50%;
    background: var(--accent); margin: 0 auto 18px;
  }
  .brand-mark .name { font-weight: 700; font-size: 28px; line-height: 32px; color: #2b2b2b; }

  .contact { position: absolute; left: 533px; top: 790px; }
  .contact-name { font-weight: 700; font-size: 27px; color: var(--accent); letter-spacing: 0.4px; }
  .contact p { font-size: 24px; color: var(--ink-soft); margin-top: 19px; line-height: 26px; }
  .contact a { color: var(--ink-soft); text-decoration: underline; }

  .sheet-label {
    position: absolute; top: 1078px; left: 0; width: 1174px; text-align: center;
    font-size: 30px; color: #111;
  }
</style>
</head>
<body>
  <main class="brochure-back">
    <section class="project">
      <div class="project-photo toorak" role="img" aria-label="Photo of a two-storey home at dusk with a lit rectangular pool and timber decking"></div>
      <div class="project-copy toorak">
        <h2 class="project-title">TOORAK LANDSCAPING</h2>
        <p class="project-tagline">Refined &amp; Structured</p>
        <div class="project-details">
          <p>Project Details:</p>
          <ul>
            <li>Front and rear entrance structured paving and planting</li>
            <li>Timber pool decking with designated entertaining platform</li>
            <li>Lawn Installation &amp; Maintenance</li>
            <li>Grass sectional pathway</li>
            <li>Fence lined espaliers</li>
            <li>Inground trampoline installation</li>
          </ul>
        </div>
      </div>
    </section>

    <div class="fold-line first"></div>

    <section class="project">
      <div class="project-photo parkville" role="img" aria-label="Photo of a courtyard garden with timber fencing, spotted gum decking and gravel planting"></div>
      <div class="project-copy parkville">
        <h2 class="project-title">PARKVILLE LANDSCAPING</h2>
        <p class="project-tagline">Lifestyle + Environment</p>
        <div class="project-details">
          <p>Project Details:</p>
          <ul>
            <li>Spotted Gum decking with trap door cellar access</li>
            <li>Ashlar lichen paving</li>
            <li>Soil conditioning for year-round edible garden</li>
            <li>Bluestone pitch paving</li>
            <li>Ground prep and mulching</li>
          </ul>
        </div>
      </div>
    </section>

    <div class="fold-line second"></div>

    <section class="contact-panel">
      <div class="brand-mark">
        <span class="dot"></span>
        <p class="name">The Ridgewell Craft<br>Premier Branch</p>
      </div>
      <div class="contact">
        <h3 class="contact-name">DALE HARTIGAN</h3>
        <p>The Ridgewell Craft • Premier Branch</p>
        <p>Postal: PO BOX 482 Westbrook VIC 3094</p>
        <p>Tel: 0400 18 36 92</p>
        <p>Email:<a href="mailto:info@theridgewellcraft.com.au">info@theridgewellcraft.com.au</a></p>
      </div>
    </section>
  </main>
  <p class="sheet-label">DL Tri-fold - Z Style - Back</p>
</body>
</html>
```